App Design Project

We are building an app and looking for design help on an existing template. We will also need a style guide. For more information, there is a website which outlines the assignment with visuals. Go here:

http://www.brivalora.com/

Industry/Entity Type

Building

```html
<!DOCTYPE html>
<html lang="en">
<head>
<meta charset="utf-8">
<title>Activities – Brivalora app screen</title>
<link rel="stylesheet" href="https://fonts.googleapis.com/css2?family=Arimo:ital,wght@0,400;0,700;1,700&family=Roboto+Condensed:wght@700&display=swap">
<style>
  :root {
    --backdrop: #3d3d3d;
    --status-black: #0c0c0c;
    --silver-hi: #fbfbfb;
    --silver-mid: #e3e3e3;
    --silver-lo: #c9c9c9;
    --ink: #555555;
    --ink-dark: #3a3a3a;
    --frame-dark: #2a2a2a;
    --glow-blue: #47c3f5;
    --panel-navy: #061a26;
    --text-blue: #1a8ad6;
    --alert-red: #e0191f;
    --led-green: #2fe03a;
    --led-red: #f21a1a;
    --chevron-green: #6cc31c;
  }
  * { box-sizing: border-box; margin: 0; padding: 0; }
  html, body { width: 1200px; height: 2281px; overflow: hidden; }
  body { background: var(--backdrop); font-family: "Arimo", Arial, sans-serif; position: relative; }

  .screen {
    position: absolute; left: 21px; top: 259px;
    width: 626px; height: 953px;
    transform: scale(1.85); transform-origin: 0 0;
    background: var(--silver-mid); overflow: hidden;
  }

  /* status bar */
  .status-bar {
    position: absolute; left: 0; top: 0; width: 626px; height: 44px;
    background: var(--status-black); color: #eee;
    font-weight: 700; font-size: 23px;
  }
  .status-bar .signal { position: absolute; left: 8px; top: 13px; }
  .status-bar .carrier { position: absolute; left: 52px; top: 10px; letter-spacing: .5px; }
  .status-bar .network { position: absolute; left: 156px; top: 10px; }
  .status-bar .lock { position: absolute; left: 302px; top: 10px; }
  .status-bar .battery { position: absolute; left: 578px; top: 14px; }

  /* navigation bar */
  .nav-bar {
    position: absolute; left: 0; top: 44px; width: 626px; height: 87px;
    background: linear-gradient(#ffffff, #e6e6e6 60%, #d2d2d2);
    border-bottom: 2px solid #7a7a7a;
  }
  .nav-button {
    position: absolute; top: 12px; height: 56px;
    border-radius: 9px; border: 1px solid #9a9a9a;
    background: linear-gradient(#fafafa, #cfcfcf 55%, #b9b9b9);
    box-shadow: 0 2px 3px rgba(0,0,0,.35), inset 0 1px 0 #fff;
    font-weight: 700; font-size: 23px; color: var(--ink);
    display: flex; align-items: center; justify-content: center;
  }
  .nav-button.back { left: 22px; width: 84px; padding-left: 4px; border-radius: 4px 9px 9px 4px; }
  .back-tip { position: absolute; left: 9px; top: 12px; }
  .nav-button.edit { left: 497px; width: 116px; }
  .screen-title {
    position: absolute; left: 142px; top: 8px; width: 325px; height: 68px;
    border-radius: 11px; border: 2px solid #f0f0f0;
    background: linear-gradient(#2b2b2b, #151515);
    box-shadow: 0 0 0 1px #888, inset 0 0 18px rgba(0,0,0,.8);
    display: flex; align-items: center; justify-content: center;
    font-weight: 700; font-size: 29px; color: var(--glow-blue);
    text-shadow: 0 0 10px rgba(71,195,245,.9), 0 0 22px rgba(71,195,245,.6);
  }

  /* content area */
  .content {
    position: absolute; left: 0; top: 131px; width: 626px; height: 669px;
    background: linear-gradient(90deg, #cfcfcf, #f4f4f4 15%, #f7f7f7 85%, #cfcfcf);
  }

  .filter-dials { position: absolute; left: 0; top: 0; width: 626px; height: 170px; }
  .dial { position: absolute; top: 10px; width: 150px; height: 150px; border-radius: 50%;
    background: radial-gradient(circle, #f3f3f3 52%, #e2e2e2 62%, #f6f6f6 75%, rgba(230,230,230,0) 100%); }
  .dial.people { left: 40px; }
  .dial.groups { left: 231px; }
  .dial.both { left: 421px; }
  .dial-ring { position: absolute; left: 19px; top: 19px; width: 112px; height: 112px; border-radius: 50%;
    background: radial-gradient(circle, #4a4a4a 60%, #262626 72%, #3e3e3e 100%);
    box-shadow: 0 3px 6px rgba(0,0,0,.4); }
  .dial-face { position: absolute; left: 17px; top: 17px; width: 78px; height: 78px; border-radius: 50%;
    background: radial-gradient(circle at 50% 35%, #ffffff, #e4e4e4 60%, #bdbdbd);
    display: flex; align-items: center; justify-content: center;
    font-family: "Roboto Condensed", "Arial Narrow", sans-serif; font-size: 17px; color: #6a6a6a; letter-spacing: .5px; }
  .dial.groups .dial-face { color: var(--alert-red); }
  .dial-led { position: absolute; left: 49px; top: 5px; width: 14px; height: 14px; border-radius: 50%; }
  .dial-led.on { background: radial-gradient(circle, #b9ffb9, var(--led-green) 55%); box-shadow: 0 0 6px var(--led-green); }
  .dial-led.off { background: radial-gradient(circle, #ffb3b3, var(--led-red) 55%); box-shadow: 0 0 6px var(--led-red); }

  .search-button {
    position: absolute; top: 175px; height: 56px;
    border-radius: 8px; background: #3a3a3a;
    box-shadow: 0 2px 4px rgba(0,0,0,.4);
    padding: 7px 9px;
  }
  .search-button span {
    display: flex; height: 100%; align-items: center; justify-content: center;
    border-radius: 6px; background: linear-gradient(#ffffff, #ececec);
    font-weight: 700; font-size: 17px; letter-spacing: 1.2px; color: var(--ink-dark);
  }
  .search-button.keywords { left: 14px; width: 289px; }
  .search-button.all { left: 318px; width: 290px; }

  /* activity card */
  .activity-card {
    position: absolute; left: 14px; top: 264px; width: 594px; height: 183px;
    border-radius: 6px; background: var(--frame-dark); padding: 6px;
  }
  .activity-card .card-body {
    position: relative; width: 100%; height: 100%; border-radius: 4px;
    background: linear-gradient(#ffffff, #f1f1f1);
  }
  .tag {
    position: absolute; height: 40px; border-radius: 6px;
    background: radial-gradient(ellipse at 50% 50%, #0e4a6c, var(--panel-navy) 75%);
    border: 1px solid #000;
    display: flex; align-items: center; justify-content: center;
    font-weight: 700; font-size: 23px; letter-spacing: 1px; color: var(--glow-blue);
    text-shadow: 0 0 6px rgba(71,195,245,.7);
  }
  .tag.activity-name { left: 24px; top: 23px; width: 285px; }
  .tag.host { left: 368px; top: 23px; width: 153px; font-size: 21px; letter-spacing: .5px; }
  .activity-meta { position: absolute; left: 27px; top: 75px; font-weight: 700; font-size: 17px; line-height: 24px; color: #5e5e5e; }
  .member-badge {
    position: absolute; left: 486px; top: 82px; width: 32px; height: 31px;
    background: #0f3f5c; border: 1px solid #000;
    display: flex; align-items: center; justify-content: center;
    font-weight: 700; font-size: 18px; color: var(--glow-blue);
  }
  .card-chevron { position: absolute; left: 540px; top: 58px; }
  .expiry {
    position: absolute; left: 20px; top: 137px; width: 286px; height: 22px;
    background: #000; border: 1px solid #777;
    font-weight: 700; font-style: italic; font-size: 13px; letter-spacing: 1px; color: var(--glow-blue);
    padding: 3px 0 0 28px;
  }
  .toggle-down { position: absolute; left: 549px; top: 145px; }

  .activity-details {
    position: absolute; left: 22px; top: 441px; width: 580px; height: 108px;
    border-radius: 0 0 8px 8px; background: linear-gradient(#ffffff, #ececec);
    box-shadow: 0 2px 4px rgba(0,0,0,.3);
    padding: 16px 21px 0 39px;
    font-size: 17.5px; line-height: 24px; color: var(--text-blue); text-align: justify;
  }
  .toggle-up { position: absolute; left: 545px; top: 92px; }

  .brand-name {
    position: absolute; left: 0; top: 633px; width: 626px; text-align: center;
    font-size: 17px; letter-spacing: 3px; color: #555;
  }

  /* tab bar */
  .tab-bar { position: absolute; left: 0; top: 800px; width: 626px; height: 153px; display: flex;
    background: #9a9a9a; gap: 3px; padding: 3px 0 0 3px; }
  .tab { position: relative; flex: 1; height: 150px; background: linear-gradient(#e8e8e8, #d8d8d8); overflow: hidden; }
  .tab-ring { position: absolute; left: 50%; top: 50%; width: 146px; height: 146px; margin: -73px 0 0 -73px; border-radius: 50%;
    background: radial-gradient(circle, #eeeeee 40%, #dcdcdc 50%, #f7f7f7 62%, #d4d4d4 75%, #e0e0e0 100%);
    box-shadow: 0 2px 5px rgba(0,0,0,.2); }
  .tab-label { position: absolute; inset: 0; display: flex; align-items: center; justify-content: center; text-align: center;
    font-family: "Roboto Condensed", "Arial Narrow", sans-serif; font-size: 19px; line-height: 21px; color: #555; }
  .tab.messages .tab-label { color: var(--alert-red); }
</style>
</head>
<body>
<main class="screen">
  <header class="status-bar">
    <svg class="signal" width="40" height="18" viewBox="0 0 40 18" aria-hidden="true">
      <rect x="0" y="14" width="5" height="4" fill="#eee"/><rect x="7" y="11" width="5" height="7" fill="#eee"/>
      <rect x="14" y="8" width="5" height="10" fill="#eee"/><rect x="21" y="4" width="5" height="14" fill="#eee"/>
      <rect x="28" y="0" width="5" height="18" fill="#eee"/>
    </svg>
    <span class="carrier">NIMBUS</span>
    <span class="network">3G</span>
    <svg class="lock" width="20" height="24" viewBox="0 0 20 24" aria-hidden="true">
      <path d="M4 11V7a6 6 0 0 1 12 0v4" fill="none" stroke="#ddd" stroke-width="3"/>
      <rect x="1" y="11" width="18" height="13" rx="2" fill="#ddd"/>
    </svg>
    <svg class="battery" width="40" height="18" viewBox="0 0 40 18" aria-hidden="true">
      <rect x="1" y="1" width="34" height="16" rx="2" fill="none" stroke="#ddd" stroke-width="2"/>
      <rect x="4" y="4" width="28" height="10" fill="#ddd"/><rect x="36" y="6" width="3" height="6" fill="#ddd"/>
    </svg>
  </header>

  <nav class="nav-bar">
    <svg class="back-tip" width="16" height="56" viewBox="0 0 16 56" aria-hidden="true" style="top:12px">
      <path d="M16 0 L0 28 L16 56 Z" fill="#d6d6d6" stroke="#9a9a9a"/>
    </svg>
    <div class="nav-button back">Back</div>
    <h1 class="screen-title">ACTIVITIES</h1>
    <div class="nav-button edit">Edit</div>
  </nav>

  <section class="content">
    <div class="filter-dials">
      <div class="dial people"><div class="dial-ring"><span class="dial-led on"></span><div class="dial-face">PEOPLE</div></div></div>
      <div class="dial groups"><div class="dial-ring"><span class="dial-led off"></span><div class="dial-face">GROUPS</div></div></div>
      <div class="dial both"><div class="dial-ring"><span class="dial-led on"></span><div class="dial-face">BOTH</div></div></div>
    </div>

    <div class="search-button keywords"><span>SEARCH BY KEYWORDS</span></div>
    <div class="search-button all"><span>SEARCH ALL ACTIVITIES</span></div>

    <article class="activity-card">
      <div class="card-body">
        <div class="tag activity-name">RACKETBALL</div>
        <div class="tag host">jorenv42</div>
        <p class="activity-meta">Allday Gym<br>January 12, 7:00 am</p>
        <div class="member-badge">M</div>
        <svg class="card-chevron" width="34" height="48" viewBox="0 0 34 48" aria-hidden="true">
          <path d="M6 4 L28 24 L6 44" fill="none" stroke="var(--chevron-green)" stroke-width="8" stroke-linejoin="miter"/>
        </svg>
        <div class="expiry">EXPIRES IN 6 HRS, 39 MINS</div>
        <svg class="toggle-down" width="22" height="11" viewBox="0 0 22 11" aria-hidden="true"><path d="M0 0 H22 L11 11 Z" fill="#555"/></svg>
      </div>
    </article>

    <div class="activity-details">
      Lorem ipsum dolor sit amet, consectetuer adipiscing elit, sed diam nonummy &nbsp;consectetuer adipiscing elit, sed diam nonummy nibh euismod tincidunt ut laoreet dolore
      <svg class="toggle-up" width="22" height="11" viewBox="0 0 22 11" aria-hidden="true"><path d="M0 11 H22 L11 0 Z" fill="#555"/></svg>
    </div>

    <p class="brand-name">BRIVALORA</p>
  </section>

  <footer class="tab-bar">
    <div class="tab"><div class="tab-ring"></div><span class="tab-label">NEW<br>SEARCH</span></div>
    <div class="tab"><div class="tab-ring"></div><span class="tab-label">NEW<br>POST</span></div>
    <div class="tab messages"><div class="tab-ring"></div><span class="tab-label">MSGS</span></div>
    <div class="tab"><div class="tab-ring"></div><span class="tab-label">MORE</span></div>
  </footer>
</main>
</body>
</html>
```